Website for an AdOps/Media Agency

We need a logo for an ad operations firm. We help websites to maximize their advertising revenues by optimizing their ad networks, configurations, technologies, etc. The name is Zornival, or ZorNival, to communicate that we take them to the top of their revenue potential. We want to also communicate, trust us to handle your adops, we take care of the hassle (it's an industry in continual technological innovation -- hard to stay on top of, and heavily manual, reporting, etc) and make sure our clients maximize ad revenues. For more info on site ideas/desires: https://files.brelmora.com/doc/7QxTbn2Lw9Rk4Vz8Hc3Md6Fp1Ys5Ga0Je/view?usp=sharing
Updates

Project Deadline Extended Reason: Apologies, I got caught up in other things. This is now priority, and will be guaranteed. I will also include an extra coding fee for a WP site and increase the budget. Thanks for your understanding! Added Thursday, July 7, 2016

Target Market(s)

Ad Operations/Media Consultancy

Industry/Entity Type

Ad Agency

Number of Pages Required

1 page

Font styles to use
Sans Serif

Requirements
Must have
• I like clean and simple, nice images, scrolling down.
Nice to have
• I like clean, fresh white running through the site. Note, I listed us as an ad agency, but only because there was no adops. We work with ad agencies, but we are more agents for publishers.
Should not have
• To much clutter.

```html
<!DOCTYPE html>
<html lang="en">
<head>
<meta charset="utf-8">
<title>Zornival — AdOps for Publishers</title>
<link href="https://fonts.googleapis.com/css2?family=Open+Sans:wght@300;400;600;700&display=swap" rel="stylesheet">
<style>
:root{
  --orange:#f7941d;
  --blue:#4a8fd8;
  --footer:#4b8fdc;
  --ink:#333840;
  --body:#5a5f66;
  --muted:#8b9097;
  --line:#e6e8eb;
  --field:#f3f4f5;
  --white:#ffffff;
}
*{margin:0;padding:0;box-sizing:border-box}
html,body{width:1200px;height:2894px;overflow:hidden}
body{font-family:"Open Sans",Arial,sans-serif;color:var(--body);background:var(--white);position:relative}
.abs{position:absolute}

/* header */
.site-header{position:absolute;left:0;top:0;width:1200px;height:84px;border-top:4px solid var(--orange);background:var(--white);box-shadow:0 1px 3px rgba(0,0,0,.06);z-index:2}
.brand{position:absolute;left:160px;top:26px;display:flex;align-items:center;gap:8px;font-weight:700;font-size:24px;color:var(--blue);letter-spacing:1px}
.brand-mark{width:18px;height:18px;background:var(--orange)}
.main-nav{position:absolute;top:36px;left:486px;display:flex;gap:0;font-size:11px;font-weight:600;color:var(--ink);text-transform:uppercase}
.main-nav a{color:inherit;text-decoration:none;position:absolute;white-space:nowrap}
.main-nav .active{color:var(--orange)}
.nav-pointer{position:absolute;left:496px;top:72px}
.demo-btn{position:absolute;left:895px;top:26px;width:143px;height:36px;background:var(--orange);color:var(--white);font-size:11px;font-weight:600;display:flex;align-items:center;justify-content:center;text-transform:uppercase;border-radius:2px}

/* hero */
.hero{position:absolute;left:0;top:84px;width:1200px;height:498px;background:linear-gradient(180deg,#2f74d0 0%,#6aa5e6 35%,#c9dbe9 55%,#7a7f84 75%,#6b5236 100%)}
.hero-title{position:absolute;left:162px;top:168px;width:500px;font-weight:300;font-size:36px;line-height:1.33;color:var(--white)}
.slider-arrow{position:absolute;width:50px;height:50px;border-radius:50%;background:rgba(40,40,40,.55);display:flex;align-items:center;justify-content:center}
.slider-arrow.light{background:rgba(150,150,150,.7)}

/* intro blocks */
.intro-title{font-size:21px;font-weight:400;color:var(--ink);line-height:1.45}
.intro-text{font-size:12px;line-height:1.75;color:var(--body);margin-top:14px}
.read-more{display:block;margin-top:16px;font-size:12px;color:var(--orange);text-transform:uppercase;letter-spacing:.3px}
.photo{position:absolute}

/* services */
.divider{position:absolute;left:162px;top:1195px;width:876px;height:1px;background:var(--line)}
.section-title{position:absolute;left:0;width:1200px;text-align:center;font-size:22px;font-weight:400;color:var(--ink)}
.section-lead{position:absolute;left:0;width:1200px;text-align:center;font-size:12px;line-height:1.7;color:var(--body)}
.service{position:absolute;width:420px;display:flex;gap:16px}
.service-icon{flex:0 0 74px;height:74px;border-radius:50%;background:var(--blue);display:flex;align-items:center;justify-content:center}
.service h3{font-size:15.5px;font-weight:400;color:var(--ink);line-height:1.3;margin-top:2px}
.service p{font-size:11px;line-height:1.65;color:var(--body);margin-top:8px}

/* contact */
.field{position:absolute;left:162px;width:422px;height:40px;background:var(--field);border:1px solid var(--line);font-size:11px;color:var(--ink);padding:12px 14px}
.submit-btn{position:absolute;left:162px;top:2754px;width:86px;height:34px;background:var(--orange);color:var(--white);font-size:11px;font-weight:600;display:flex;align-items:center;justify-content:center;text-transform:uppercase}
.map{position:absolute;left:622px;top:2512px;width:416px;height:276px;background:linear-gradient(135deg,#e9e4d3,#d9dcc8);border:1px solid var(--line)}
.map-pin{position:absolute;left:182px;top:112px;width:52px;height:52px;border-radius:50%;background:var(--blue);display:flex;align-items:center;justify-content:center}

/* footer */
.site-footer{position:absolute;left:0;top:2824px;width:1200px;height:70px;background:var(--footer)}
.social{position:absolute;left:162px;top:22px;display:flex;gap:6px}
.social span{width:28px;height:28px;border:1.5px solid rgba(255,255,255,.85);border-radius:50%}
.footer-brand{position:absolute;left:356px;top:20px;font-size:24px;font-weight:700;color:var(--white);letter-spacing:1px}
.copyright{position:absolute;left:736px;top:28px;font-size:10.5px;color:var(--white)}
</style>
</head>
<body>

<header class="site-header">
  <div class="brand"><span class="brand-mark"></span>ZORNIVAL</div>
  <nav class="main-nav">
    <a class="active" style="left:0">Home</a>
    <a style="left:90px">About</a>
    <a style="left:184px">Services</a>
    <a style="left:290px">Free Consult</a>
  </nav>
  <svg class="nav-pointer" width="14" height="10" viewBox="0 0 14 10"><path d="M1 9 7 2 13 9" fill="none" stroke="#f7941d" stroke-width="1.5"/></svg>
  <div class="demo-btn">Request a Demo&nbsp;›</div>
</header>

<section class="hero" role="img" aria-label="Hiker with raised arms on a mountain ridge under blue sky with snowy peaks">
  <h1 class="hero-title">Onestop shop for all your adops needs Digital Monetization Maximization.</h1>
  <div class="slider-arrow" style="left:20px;top:224px"><svg width="12" height="14"><path d="M9 2 3 7 9 12" fill="none" stroke="#fff" stroke-width="2"/></svg></div>
  <div class="slider-arrow" style="left:1130px;top:224px"><svg width="12" height="14"><path d="M3 2 9 7 3 12" fill="none" stroke="#fff" stroke-width="2"/></svg></div>
</section>

<section class="abs" style="left:162px;top:632px;width:400px">
  <h2 class="intro-title">Let our team help YOUR team Optimize your adops and &nbsp;maximize your monetization</h2>
  <p class="intro-text">We can help you take your revenues to the next level. Our team will work handinhand with your team to ensure that things run smoothly, optimally, and for the best possible returns.</p>
  <a class="read-more">Read More</a>
</section>
<div class="photo" style="left:600px;top:614px;width:438px;height:249px;background:linear-gradient(160deg,#5a5650,#a8a49c 45%,#e9eaec 80%)" role="img" aria-label="Climbers with backpacks ascending a rocky snowy slope"></div>

<div class="photo" style="left:162px;top:898px;width:438px;height:249px;background:linear-gradient(180deg,#cfdbe6,#f2f5f8 55%,#dfe6ee)" role="img" aria-label="Group of trekkers with colourful backpacks walking through snow"></div>
<section class="abs" style="left:640px;top:920px;width:410px">
  <h2 class="intro-title">Publisher Partnership</h2>
  <p class="intro-text">Programmatic has revolutionized the advertising playing field. Now, small, medium and large publishers a like all have equal access to the best advertisers and premium cpms. But it's a fast moving world, and it takes a big team and varied skill set to stay on top of the technologies, players, offers, implementations and optimizations. Our team covers all these skills, and our team wants to be on your team</p>
  <a class="read-more">Read More</a>
</section>

<div class="divider"></div>

<h2 class="section-title" style="top:1226px">AdOps Optimization</h2>
<p class="section-lead" style="top:1270px">Leave it to us to streamline, optimize, and manage your ad network relationships<br>and operations. We'll help you take your revenues to the next level:</p>

<!-- services: left column -->
<div class="service" style="left:162px;top:1348px">
  <div class="service-icon"><svg width="30" height="30" viewBox="0 0 30 30"><path d="M6 24l2-7 12-12 5 5-12 12z" fill="#fff"/></svg></div>
  <div><h3>Monetization Strategy &amp; Planning</h3><p>There's no "one size fits all" ads strategy. We help you find the winning combination,placements and mix for your adspace offer.</p></div>
</div>
<div class="service" style="left:162px;top:1470px">
  <div class="service-icon"><svg width="30" height="30" viewBox="0 0 30 30"><circle cx="15" cy="15" r="9" fill="none" stroke="#fff" stroke-width="3"/></svg></div>
  <div><h3>Access to our Premium Vantrel Exchange Account</h3><p>Get the same rates as the big guys, with individualized, ongoing exchange optimization in our Vantrel partner account, including access to our select premium marketplace.</p></div>
</div>
<div class="service" style="left:162px;top:1596px">
  <div class="service-icon"><svg width="30" height="30" viewBox="0 0 30 30"><circle cx="15" cy="15" r="8" fill="none" stroke="#fff" stroke-width="4" stroke-dasharray="3 2"/><circle cx="15" cy="15" r="3" fill="#fff"/></svg></div>
  <div><h3>Ad server setup, training &amp; troubleshooting</h3><p>Video, Native, Header Bidding, Display...we stay on top of the technologies, so you don't have to</p></div>
</div>
<div class="service" style="left:162px;top:1694px">
  <div class="service-icon"><svg width="30" height="30" viewBox="0 0 30 30"><path d="M4 14 26 5 19 26 14 17z" fill="#fff"/></svg></div>
  <div><h3>Campaign Performance &amp; Reporting</h3><p>Daily reporting, continuous monitoring for performance and discrepancies.</p></div>
</div>
<div class="service" style="left:162px;top:1804px">
  <div class="service-icon"><svg width="30" height="30" viewBox="0 0 30 30"><path d="M5 12h5l11-6v18l-11-6H5z" fill="#fff"/></svg></div>
  <div><h3>Ongoing Optimization</h3><p>The Holy Grail. We never stop tweaking and tightening to keep your revenues optimized and adjusted for seasonal fluctuations.</p></div>
</div>
<div class="service" style="left:162px;top:1910px">
  <div class="service-icon"><svg width="30" height="30" viewBox="0 0 30 30"><circle cx="15" cy="10" r="5" fill="#fff"/><path d="M6 25c0-6 4-9 9-9s9 3 9 9z" fill="#fff"/></svg></div>
  <div><h3>Direct Advertiser Management</h3><p>We field &amp; manage your direct advertiser enquiries and campaigns.</p></div>
</div>

<!-- services: right column -->
<div class="service" style="left:627px;top:1348px">
  <div class="service-icon"><svg width="30" height="30" viewBox="0 0 30 30"><circle cx="15" cy="15" r="10" fill="#fff"/></svg></div>
  <div><h3>Network Configurations</h3><p>From header bidders, to video, to native, to display, we create your optimum mix for maximum monetization: Screening, implementation, testing, measurement, and ongoing optimization to keep revenues at a max.</p></div>
</div>
<div class="service" style="left:627px;top:1470px">
  <div class="service-icon"><svg width="32" height="30" viewBox="0 0 32 30"><circle cx="9" cy="11" r="4" fill="#fff"/><circle cx="23" cy="11" r="4" fill="#fff"/><circle cx="16" cy="9" r="4.5" fill="#fff"/><path d="M3 23c0-4 3-6 6-6s6 2 6 6zM17 23c0-4 3-6 6-6s6 2 6 6zM9 24c0-5 3-8 7-8s7 3 7 8z" fill="#fff"/></svg></div>
  <div><h3>Contract Negotiation, Relationship Management</h3><p>We help to make sure you are getting the best possible pricing and terms, and keep the relations to make sure the premium offers keep coming your way.</p></div>
</div>
<div class="service" style="left:627px;top:1596px">
  <div class="service-icon"><svg width="30" height="30" viewBox="0 0 30 30"><path d="M5 5h10l11 11-10 10L5 15z" fill="#fff"/><circle cx="10" cy="10" r="2" fill="#4a8fd8"/></svg></div>
  <div><h3>Ad tag implementation &amp; tracking</h3><p>Let us take care of the details: orders, CPMs, scheduling, targeting, volumes, frequency caps.</p></div>
</div>
<div class="service" style="left:627px;top:1694px">
  <div class="service-icon"><svg width="30" height="30" viewBox="0 0 30 30"><path d="M5 5v20h21" fill="none" stroke="#fff" stroke-width="2"/><rect x="9" y="14" width="3" height="9" fill="#fff"/><rect x="14" y="9" width="3" height="14" fill="#fff"/><rect x="19" y="12" width="3" height="11" fill="#fff"/></svg></div>
  <div><h3>Audience Segmentation, Targeting &amp; Marketing</h3><p>Target, segment, package &amp; sell your audiences to the right advertisers for maximum revenues</p></div>
</div>
<div class="service" style="left:627px;top:1804px">
  <div class="service-icon"><svg width="30" height="30" viewBox="0 0 30 30"><path d="M8 4h10l5 5v17H8z" fill="#fff"/><path d="M12 14h7M12 18h7" stroke="#4a8fd8" stroke-width="2"/></svg></div>
  <div><h3>Quality Control</h3><p>We work with you to keep bad ads out, and block lists uptodate.</p></div>
</div>
<div class="service" style="left:627px;top:1910px">
  <div class="service-icon"><svg width="30" height="30" viewBox="0 0 30 30"><rect x="4" y="9" width="22" height="16" rx="2" fill="#fff"/><path d="M11 9V6h8v3" fill="none" stroke="#fff" stroke-width="2"/></svg></div>
  <div><h3>Business Development</h3><p>We stay on top of the latest trends and best technologies, so you don't have to!</p></div>
</div>

<section class="abs" style="left:0;top:2050px;width:1200px;height:310px;background:linear-gradient(180deg,#5d8fc9,#b9cde0 55%,#8a96a3 80%,#4c4640)" role="img" aria-label="Hiker with outstretched arms on a rocky summit above a snowy mountain range">
  <div class="slider-arrow light" style="left:20px;top:130px"><svg width="12" height="14"><path d="M9 2 3 7 9 12" fill="none" stroke="#fff" stroke-width="2"/></svg></div>
  <div class="slider-arrow light" style="left:1130px;top:130px"><svg width="12" height="14"><path d="M3 2 9 7 3 12" fill="none" stroke="#fff" stroke-width="2"/></svg></div>
</section>

<h2 class="section-title" style="top:2396px;text-transform:uppercase">Let's keep in touch contact us</h2>
<p class="section-lead" style="top:2438px">Sed ut perspiciatis unde omnis iste natus error sit voluptatem accusantium doloremque laudantium, totam rem aperiam,<br>eaque ipsa quae ab illo inventore veritatis et quasi architecto beatae vitae dicta sunt explicabo.</p>

<div class="field" style="top:2512px">Name:</div>
<div class="field" style="top:2558px">Email:</div>
<div class="field" style="top:2604px">Phone:</div>
<div class="field" style="top:2652px;height:94px">Message:</div>
<div class="submit-btn">Submit&nbsp;›</div>

<div class="map" role="img" aria-label="Street map of the office location">
  <div class="map-pin"><svg width="18" height="22" viewBox="0 0 18 22"><path d="M9 1a7 7 0 0 0-7 7c0 5 7 13 7 13s7-8 7-13a7 7 0 0 0-7-7z" fill="#fff"/><circle cx="9" cy="8" r="2.5" fill="#4a8fd8"/></svg></div>
</div>

<footer class="site-footer">
  <div class="social"><span></span><span></span><span></span><span></span><span></span></div>
  <div class="footer-brand">ZORNIVAL</div>
  <p class="copyright">© 2016 All copyrights reserved.Zornival. Terms and Conditions</p>
</footer>

</body>
</html>
```